Business Card Design

We are a Sydney based bespoke Concierge company, providing hospitality services including Concierge staffing, catering, home dining, events, delivery, stallorix, and manage desks in residential apartment services. Our website goes into more detail.

Target Market(s)

corporate clients, upscale residential clients, executives,

Industry/Entity Type

Hospitality

Contact Information for Business Card

David SouthwellDirector of Operations & Customer Experience
Marlowe Concierge
W:www.marloweconcierge-demo.net;
E;peter@marloweconcierge-demo.net
M: 0412 907 281

Font styles to use
Serif

Colors
3176b5
85cae6
d2a4cc
6b449b

Requirements
Must have
• Business name
• Name
• Title
• Tel
• Email
• Website
Nice to have
• Back - facebook , twitter, instagram

```html
<!DOCTYPE html>
<html lang="en">
<head>
<meta charset="utf-8">
<title>Marlowe Concierge – Business Card</title>
<link rel="stylesheet" href="https://fonts.googleapis.com/css2?family=Arimo&family=Open+Sans:wght@400&family=Source+Sans+3:wght@400&display=swap">
<style>
  :root {
    --blue: #3176b5;
    --sky: #85cae6;
    --pink: #d2a4cc;
    --purple: #6b449b;
    --backdrop: #c4c8d2;
  }
  * { margin: 0; padding: 0; box-sizing: border-box; }
  html, body {
    width: 1200px; height: 1000px; overflow: hidden;
    background: var(--backdrop);
  }
  .stage { position: relative; width: 1200px; height: 1000px; }
  .card { position: absolute; width: 840px; height: 478px; overflow: hidden; }

  /* Front */
  .card-front { left: 45px; top: 40px; background: var(--blue); z-index: 2; }
  .front-stripe {
    position: absolute; left: 105px; top: 0; width: 30px; height: 100%;
    background: linear-gradient(to bottom, var(--purple) 0%, var(--purple) 15%, #4f5fab 35%, #4f5fab 60%, var(--purple) 80%, var(--purple) 100%);
  }
  .holder-name {
    position: absolute; left: 62px; top: 138px;
    font: 34px "Arimo", sans-serif; color: var(--sky); white-space: nowrap;
  }
  .holder-title {
    position: absolute; left: 62px; top: 181px;
    font: 22px "Open Sans", sans-serif; color: var(--pink);
    letter-spacing: 0.6px; white-space: nowrap;
  }
  .front-brand {
    position: absolute; left: 428px; top: 282px;
    font: 27px "Source Sans 3", sans-serif; color: var(--sky); white-space: nowrap;
  }
  .contact-list { position: absolute; left: 426px; top: 324px; list-style: none; }
  .contact-item {
    display: flex; align-items: center; height: 33px; white-space: nowrap;
    font: 22px "Source Sans 3", sans-serif; color: var(--sky);
  }
  .contact-icon { width: 28px; height: 26px; margin-right: 19px; flex: none; }

  /* Back */
  .card-back { left: 323px; top: 476px; background: var(--purple); z-index: 1; }
  .back-band {
    position: absolute; left: 0; top: 214px; width: 100%; height: 49px;
    background: linear-gradient(to right, var(--blue) 0%, var(--blue) 12%, #5a55a6 28%, #5a55a6 72%, var(--blue) 88%, var(--blue) 100%);
    display: flex; align-items: center; justify-content: center;
    font: 27px "Source Sans 3", sans-serif; color: var(--sky);
  }
  .social-row { position: absolute; top: 392px; left: 0; width: 100%; height: 26px; }
  .social-item {
    position: absolute; top: 0; display: flex; align-items: center; height: 26px;
    font: 19px "Source Sans 3", sans-serif; color: var(--sky); white-space: nowrap;
  }
  .social-mark {
    width: 24px; height: 24px; background: var(--pink); margin-right: 9px; flex: none;
  }
  .social-item.social-page { left: 63px; }
  .social-item.social-handle-first { left: 340px; }
  .social-item.social-handle-second { left: 598px; }
</style>
</head>
<body>
<main class="stage">
  <section class="card card-front" aria-label="Business card front">
    <div class="front-stripe"></div>
    <h1 class="holder-name">Peter Hollingby</h1>
    <p class="holder-title">Director of Operations &amp; Costumer Experience</p>
    <p class="front-brand">Marlowe Concierge</p>
    <ul class="contact-list">
      <li class="contact-item">
        <svg class="contact-icon" viewBox="0 0 28 26" aria-hidden="true">
          <rect x="8" y="1" width="12" height="24" rx="2" fill="none" stroke="var(--pink)" stroke-width="2"/>
          <line x1="11" y1="21" x2="17" y2="21" stroke="var(--pink)" stroke-width="2"/>
        </svg>0412 907 281
      </li>
      <li class="contact-item">
        <svg class="contact-icon" viewBox="0 0 28 26" aria-hidden="true">
          <rect x="0" y="6" width="28" height="16" fill="var(--pink)"/>
          <polyline points="0,6 14,15 28,6" fill="none" stroke="var(--blue)" stroke-width="2"/>
        </svg>peter@marloweconcierge-demo.net
      </li>
      <li class="contact-item">
        <svg class="contact-icon" viewBox="0 0 28 26" aria-hidden="true">
          <g fill="none" stroke="var(--pink)" stroke-width="2">
            <circle cx="14" cy="13" r="11"/>
            <ellipse cx="14" cy="13" rx="5" ry="11"/>
            <line x1="3" y1="13" x2="25" y2="13"/>
            <line x1="5" y1="7" x2="23" y2="7"/>
            <line x1="5" y1="19" x2="23" y2="19"/>
          </g>
        </svg>www.marloweconcierge-demo.net
      </li>
    </ul>
  </section>

  <section class="card card-back" aria-label="Business card back">
    <div class="back-band"><span>Marlowe Concierge</span></div>
    <div class="social-row">
      <p class="social-item social-page"><span class="social-mark"></span>Marlowe Concierge</p>
      <p class="social-item social-handle-first"><span class="social-mark"></span>@marloweconcierge</p>
      <p class="social-item social-handle-second"><span class="social-mark"></span>@marloweconcierge</p>
    </div>
  </section>
</main>
</body>
</html>
```